Women Web Portal

We are developing an internet portal with content created by and for women in Latin America.
This portal will contain different categories focused on relevant topics for women who are at the same time mothers, lovers, workers, pet-owners, ...

We are looking for design that are at the same time uncluttered, easy-to-use and obvious, and comfy. Pastel colours, buttons using traditional fonts, large space for pictures, highlighted social elements,...

Our target being the middle-class women, we want a design that feels comfortable, real, a bit trendy and traditional, not a Vestry & Holm design, something women can relate to and feel comfortable enough to come back and participate.

Examples of websites:
www.cookvault.example
dama.portalvix.example
www.cabellorivo.example
www.casserol.example
Updates

Hi dear designers. After viewing some first drafts, I have updated the brief so you might have a better understanding of what we are looking for.

Thanks

Reason: We've been away for a while, unavailable to provide adequate feedback to the designs already sent. So we're extending the deadline in order to give time to everyone to adapt their work according to the feedback we'll be providing today.

Target Market(s)

Women between 25 and 50 years from Latin America. Mainly mothers: basically, we want women to interact with each other and with the content of the site so they create a strong community.

Advertisingly speaking, we want to have users, contents and FMCG brands to live together on this website.

Industry/Entity Type

Internet

Requirements
Must have
• Pastel colours for category tabs. Comfortable look & feel.

The design should include 3 different pages:
- Homepage
- Article page
- User profile

The page will be done in responsive design, so design should be thought to be adapted according to the browser (2 or 3 columns).

Thanks for doing it as a PSD file .

The design should also include:
- 8 category tabs
- Space for 728x90px and 300x600px advertising format.
- A relevant menu bar at the beginning of each page
Nice to have
• News feed/best content/most active comments zone: we need to bring forward content to our users so they'll be attracted to visit more pages of the website.

Small format to register (account).

Slider or any other moving objects.

Any idea that would facilitate and increase user participation
Should not have
• Actual text. please use Lorem Ipsum.

```html
<!DOCTYPE html>
<html lang="en">
<head>
<meta charset="utf-8">
<title>Women Portal – Home</title>
<link rel="stylesheet" href="https://fonts.googleapis.com/css2?family=Sorts+Mill+Goudy&display=swap">
<style>
  :root {
    --teal: #187c80;
    --cream: #fcf9f3;
    --ink: #4f4f4f;
    --white: #ffffff;
    --rule: #d9d6cf;
    --ad-red: #a41f24;
    --ad-ink: #222222;
    --muted: #8a8a8a;
    --sun: #f2b233;
  }
  * { box-sizing: border-box; margin: 0; padding: 0; }
  html, body { width: 1200px; height: 1200px; overflow: hidden; }
  body {
    position: relative;
    background: var(--cream);
    font-family: "Sorts Mill Goudy", Georgia, serif;
    color: var(--ink);
  }

  .top-bar {
    position: absolute; left: 0; top: 0; width: 1200px; height: 87px;
    background: var(--teal); color: var(--white); font-size: 17px;
  }
  .account-links { position: absolute; left: 174px; top: 38px; display: flex; gap: 16px; }
  .account-links .divider { width: 1px; height: 20px; background: var(--white); margin-top: 1px; }
  .live-chat { position: absolute; left: 898px; top: 38px; display: flex; align-items: center; gap: 12px; }
  .live-chat svg { margin-top: -2px; }
  .search-button {
    position: absolute; left: 1049px; top: 37px; width: 23px; height: 23px;
    border-radius: 50%; background: var(--white);
  }
  .search-button svg { position: absolute; left: 6px; top: 6px; }

  .brand { position: absolute; left: 124px; top: 116px; width: 260px; height: 60px; }
  .brand-dot { position: absolute; left: 0; top: 0; width: 58px; height: 58px; border-radius: 50%; background: var(--sun); }
  .brand-name { position: absolute; left: 79px; top: 2px; font-size: 24px; color: var(--teal); line-height: 1; white-space: nowrap; }
  .brand-tagline { position: absolute; left: 81px; top: 34px; font-size: 12px; color: var(--muted); white-space: nowrap; }

  .main-nav { position: absolute; left: 0; top: 87px; width: 1200px; height: 82px; }
  .main-nav a {
    position: absolute; top: 0; height: 82px; padding-top: 46px;
    font-size: 17px; color: var(--ink); text-decoration: none; white-space: nowrap;
  }
  .main-nav a.active { background: var(--teal); color: var(--white); width: 83px; text-align: center; }

  .hero {
    position: absolute; left: 0; top: 203px; width: 1200px; height: 569px;
    background: linear-gradient(180deg, #dfe5ea 0%, #d8d4d0 45%, #c9b7a6 100%);
  }
  .hero-figure {
    position: absolute; left: 520px; top: 0; width: 640px; height: 569px;
    background: radial-gradient(ellipse at 60% 55%, #e7789a 0%, #e69bb0 40%, rgba(230,190,190,0) 75%);
  }
  .hero-card {
    position: absolute; left: 107px; top: 349px; width: 399px; height: 284px;
    background: var(--teal); color: var(--white); text-align: center;
  }
  .hero-card h2 { font-weight: normal; font-size: 26px; margin-top: 58px; }
  .hero-card p { font-size: 13.5px; line-height: 22.5px; width: 280px; margin: 18px auto 0; }
  .hero-card .next {
    position: absolute; left: 184px; top: 209px; width: 31px; height: 31px;
    border-radius: 50%; background: var(--white);
  }
  .hero-card .next svg { position: absolute; left: 10px; top: 8px; }

  .intro {
    position: absolute; left: 146px; top: 838px; width: 1000px; text-align: center;
    font-size: 38px; line-height: 44px; color: var(--ink); font-weight: normal;
  }

  .ad-leaderboard { position: absolute; left: 236px; top: 978px; width: 728px; height: 90px; display: flex; }
  .ad-claim {
    width: 225px; background: var(--ad-red); color: var(--white);
    font-size: 22px; line-height: 30px; padding: 15px 0 0 16px;
  }
  .ad-photo { width: 289px; background: linear-gradient(135deg, #c9c3b8, #e9e4da 50%, #a9a39a); }
  .ad-sponsor {
    width: 214px; background: var(--white); display: flex; flex-direction: column;
    justify-content: center; padding-left: 14px; color: var(--ad-ink);
  }
  .ad-sponsor .name { font-size: 21px; }
  .ad-sponsor .url { font-size: 9.5px; letter-spacing: 0.8px; margin-top: 8px; }

  .section-title {
    position: absolute; left: 180px; top: 1137px; font-size: 24px; font-weight: normal; color: #3f3f3f; white-space: nowrap;
  }
  .section-rule { position: absolute; left: 466px; top: 1153px; width: 560px; height: 1px; background: var(--rule); }
</style>
</head>
<body>
  <header class="top-bar">
    <nav class="account-links"><span>Log In</span><span class="divider"></span><span>Register</span></nav>
    <div class="live-chat">
      <svg width="30" height="24" viewBox="0 0 30 24" aria-hidden="true">
        <rect x="1" y="1" width="19" height="13" rx="2" fill="#fff"/>
        <rect x="8" y="6" width="20" height="13" rx="2" fill="#fff" stroke="#187c80" stroke-width="1.5"/>
        <path d="M21 19 L24 23 L24 19 Z" fill="#fff"/>
      </svg>
      <span>Live Chat</span>
    </div>
    <div class="search-button">
      <svg width="11" height="11" viewBox="0 0 11 11" aria-hidden="true">
        <circle cx="4.5" cy="4.5" r="3.2" fill="none" stroke="#187c80" stroke-width="1.4"/>
        <path d="M7 7 L10 10" stroke="#187c80" stroke-width="1.6"/>
      </svg>
    </div>
  </header>

  <div class="brand">
    <span class="brand-dot"></span>
    <div class="brand-name">Company name</div>
    <div class="brand-tagline">your tagline goes here</div>
  </div>

  <nav class="main-nav">
    <a class="active" href="#" style="left:413px">Menu 1</a>
    <a href="#" style="left:511px">Menu 2</a>
    <a href="#" style="left:597px">Menu 3</a>
    <a href="#" style="left:682px">Menu 4</a>
    <a href="#" style="left:768px">Menu 5</a>
    <a href="#" style="left:853px">Menu 6</a>
    <a href="#" style="left:939px">Menu 7</a>
    <a href="#" style="left:1024px">Menu 8</a>
  </nav>

  <section class="hero">
    <div class="hero-figure" role="img" aria-label="Photo of a smiling mother in a pink sweater hugging her young daughter on a beach"></div>
  </section>
  <div class="hero-card">
    <h2>Architecto architecto</h2>
    <p>fugit aut illo omnis explicabo ipsa ipsa, nemo rem ipsam quasi illo dolores ut voluptatem doloremque perspiciatis beatae magni</p>
    <span class="next">
      <svg width="12" height="15" viewBox="0 0 12 15" aria-hidden="true"><path d="M3 1.5 L9 7.5 L3 13.5" fill="none" stroke="#187c80" stroke-width="2.6"/></svg>
    </span>
  </div>

  <h1 class="intro">Lorem ipsum dolar sit amet voluptatem fugit aut illo<br>omnis explicabo ipsa ipsa, nemo rem ipsam</h1>

  <aside class="ad-leaderboard" aria-label="Advertisement">
    <div class="ad-claim">Readers Value<br>Local Stories</div>
    <div class="ad-photo" role="img" aria-label="Photo of people in a café reading newspapers"></div>
    <div class="ad-sponsor">
      <div class="name">Pressline Project</div>
      <div class="url">www.presslineproject.example</div>
    </div>
  </aside>

  <h2 class="section-title">Accusantium laudantium</h2>
  <div class="section-rule"></div>
</body>
</html>
```